Lawn mowing business card design

We need a business card design for our lawn mowing and gardening business which is located in the Northern Beaches of Sydney. Our business name is Meadowline Turf and our logo is predominantly green and yellow in color. Please see our website at www.meadowlineturf.com.au for design ideas. The business targets young professionals and older clientele. As such the font should be easy to read, but I also want the business card to be colorful and stand out.

Target Market(s)

young professionals

Industry/Entity Type

Lawn Care

Contact Information for Business Card

Meadowline Turf, Gareth Pellow, 0478559201, www.meadowlineturf.com.au, email: meadowlineturf@mailbox-example.com

Font styles to use
Serif

Colors
9bcb3b
fbed22

Requirements
Must have
• Must include the details listed above. Must include the attached logo.
Nice to have
• Logo attached with two copies. The logo without any writing is high quality, please feel free to be creative with the text stating our business name "Meadowline Turf" using this file.

```html
<!DOCTYPE html>
<html lang="en">
<head>
<meta charset="utf-8">
<title>Meadowline Turf – Business Card</title>
<link rel="stylesheet" href="https://fonts.googleapis.com/css2?family=Roboto:wght@400;500;700&display=swap">
<style>
  :root {
    --page-bg: #e9ece8;
    --green-front: #2f9e4a;
    --green-front-dark: #23873c;
    --green-dark: #1d8a3d;
    --green-deep: #167232;
    --green-light: #8dc63f;
    --green-lime: #a6d44a;
    --yellow: #fbed22;
    --white: #ffffff;
    --ink-green: #1b7d37;
    --shadow: rgba(0, 0, 0, 0.18);
  }
  * { box-sizing: border-box; margin: 0; padding: 0; }
  html, body { width: 1200px; height: 950px; overflow: hidden; }
  body {
    background: var(--page-bg);
    font-family: "Roboto", Arial, sans-serif;
    position: relative;
  }
  .card {
    position: absolute;
    left: 240px;
    width: 720px;
    height: 410px;
    overflow: hidden;
    box-shadow: 0 10px 28px var(--shadow);
  }

  /* Front side */
  .card-front {
    top: 45px;
    background: linear-gradient(160deg, var(--green-front) 0%, var(--green-front-dark) 100%);
    color: var(--white);
  }
  .front-brand {
    position: absolute;
    left: 0; right: 0; top: 130px;
    display: flex; align-items: center; justify-content: center; gap: 16px;
  }
  .brand-dot {
    width: 26px; height: 26px; border-radius: 50%;
    background: var(--yellow);
  }
  .brand-name {
    font-size: 44px; font-weight: 700; letter-spacing: 0.5px;
  }
  .front-url {
    position: absolute;
    left: 0; right: 0; top: 300px;
    text-align: center;
    font-size: 20px; letter-spacing: 1px;
  }

  /* Back side */
  .card-back {
    top: 495px;
    background: var(--white);
  }
  .back-brand {
    position: absolute;
    left: 0; right: 0; top: 70px;
    display: flex; align-items: center; justify-content: center; gap: 14px;
  }
  .back-brand .brand-name { color: var(--ink-green); font-size: 36px; }
  .back-brand .brand-dot { background: var(--green-light); width: 22px; height: 22px; }

  .band-light {
    position: absolute;
    left: 0; right: 0; top: 190px; height: 100px;
    background: linear-gradient(90deg, var(--green-lime), var(--green-light));
  }
  .band-dark {
    position: absolute;
    left: 0; right: 0; top: 290px; bottom: 0;
    background: linear-gradient(90deg, var(--green-dark), var(--green-deep));
  }
  .person {
    position: absolute;
    left: 0; right: 0; top: 206px;
    text-align: center;
  }
  .person-name {
    font-size: 30px; font-weight: 700; color: var(--ink-green);
  }
  .person-title {
    font-size: 19px; color: var(--white); margin-top: 4px;
  }
  .contacts {
    position: absolute;
    left: 0; right: 0; top: 310px;
    color: var(--white);
    font-size: 19px;
    display: flex; flex-direction: column; align-items: center; gap: 14px;
  }
  .contact-row { display: flex; align-items: center; gap: 22px; }
  .contact-item { display: flex; align-items: center; gap: 8px; }
  .contact-item svg { width: 20px; height: 20px; fill: var(--white); flex: none; }
</style>
</head>
<body>

  <section class="card card-front" aria-label="Business card front">
    <div class="front-brand">
      <span class="brand-dot"></span>
      <span class="brand-name">Meadowline Turf</span>
    </div>
    <p class="front-url">www.meadowlineturf.com.au</p>
  </section>

  <section class="card card-back" aria-label="Business card back">
    <div class="back-brand">
      <span class="brand-dot"></span>
      <span class="brand-name">Meadowline Turf</span>
    </div>

    <div class="band-light"></div>
    <div class="band-dark"></div>

    <div class="person">
      <p class="person-name">Gareth Pellow</p>
      <p class="person-title">President</p>
    </div>

    <div class="contacts">
      <div class="contact-row">
        <span class="contact-item">
          <svg viewBox="0 0 24 24" aria-hidden="true"><path d="M6.6 10.8a15.1 15.1 0 0 0 6.6 6.6l2.2-2.2a1 1 0 0 1 1-.25 11.4 11.4 0 0 0 3.6.57 1 1 0 0 1 1 1V20a1 1 0 0 1-1 1A17 17 0 0 1 3 4a1 1 0 0 1 1-1h3.5a1 1 0 0 1 1 1c0 1.25.2 2.45.57 3.57a1 1 0 0 1-.25 1z"/></svg>
          0478559201
        </span>
        <span class="contact-item">
          <svg viewBox="0 0 24 24" aria-hidden="true"><path d="M2 5h20v14H2z M4 7v.4l8 5 8-5V7z" fill-rule="evenodd"/></svg>
          meadowlineturf@mailbox-example.com
        </span>
      </div>
      <div class="contact-row">
        <span class="contact-item">
          <svg viewBox="0 0 24 24" aria-hidden="true"><path d="M12 2a10 10 0 1 0 0 20 10 10 0 0 0 0-20zm0 2c.9 0 2.2 1.9 2.7 5H9.3C9.8 5.9 11.1 4 12 4zM4.3 11h3a17 17 0 0 0 0 2h-3a8 8 0 0 1 0-2zm5 0h5.4a15 15 0 0 1 0 2H9.3a15 15 0 0 1 0-2zm7.4 0h3a8 8 0 0 1 0 2h-3a17 17 0 0 0 0-2zM9.3 15h5.4c-.5 3.1-1.8 5-2.7 5s-2.2-1.9-2.7-5z"/></svg>
          www.meadowlineturf.com.au
        </span>
      </div>
    </div>
  </section>

</body>
</html>
```